seeking a modern Business Card design for Roof Plumbering Business

hallowell roof plumbing is a local metal re-roof and new construction specialist. We are seeking a modern business card to assist with networking within the industry. Our services are predominantly the installation of metal roofs on new houses, however we also do re-roofs when an existing roof needs replacing. We service both residential and commercial properties. Please include the below details on the card:
Name: Owen Hallowell
Phone: 0417 382 965
Email: owenhallowellroofing@maildrop-example.com

Residential & Commercial
Re-roof & New Construction
Fully Insured

I have uploaded our business logo, which we think would suit a black background. Please use all lower case for business name.
Cheers
Updates

Hey Guys, As requested I've uploaded a Pdf version of my logo. Hopefully this help. Thanks

Industry/Entity Type

Business

Contact Information for Business Card

Name: Owen Hallowell
Phone: 0417 382 965

Residential & Commercial
Fully Insured

Font styles to use
Serif
Sans Serif

Requirements
Must have
• Name must be all lower case "hallowell roof plumbing"
Nice to have
• Stick with Logo Colours

```html
<!DOCTYPE html>
<html lang="en">
<head>
<meta charset="utf-8">
<title>hallowell roof plumbing — business card</title>
<link rel="stylesheet" href="https://fonts.googleapis.com/css2?family=EB+Garamond:wght@400;500;600&display=swap">
<style>
  :root {
    --backdrop: #2b2b2b;
    --card-black: #050505;
    --brand-blue: #2c9cd0;
    --band-blue: #2f7fae;
    --band-text: #0b1a24;
    --label-grey: #d9d9d9;
    --icon-grey: #9a9a9a;
  }
  * { margin: 0; padding: 0; box-sizing: border-box; }
  html, body {
    width: 1200px;
    height: 997px;
    overflow: hidden;
    background: var(--backdrop);
  }
  .stage {
    position: relative;
    width: 1200px;
    height: 997px;
  }
  .business-card {
    position: absolute;
    left: 180px;
    top: 258px;
    width: 840px;
    height: 480px;
    background: var(--card-black);
    border-radius: 30px;
    overflow: hidden;
    font-family: "EB Garamond", Georgia, serif;
    box-shadow: 0 18px 40px rgba(0,0,0,0.45);
  }
  .brand-lockup {
    position: absolute;
    left: 250px;
    top: 70px;
    display: flex;
    align-items: center;
    gap: 14px;
  }
  .brand-mark {
    width: 18px;
    height: 18px;
    background: var(--brand-blue);
  }
  .brand-name {
    color: var(--brand-blue);
    font-weight: 500;
    font-size: 40px;
    letter-spacing: 1px;
    line-height: 1;
  }
  .holder {
    position: absolute;
    left: 60px;
    top: 226px;
  }
  .holder-name {
    color: var(--brand-blue);
    font-weight: 600;
    font-size: 32px;
    line-height: 1.05;
  }
  .holder-role {
    color: var(--label-grey);
    font-weight: 600;
    font-size: 17px;
    margin-top: 2px;
  }
  .contact-list {
    position: absolute;
    left: 60px;
    top: 318px;
    list-style: none;
  }
  .contact-item {
    display: flex;
    align-items: center;
    gap: 16px;
    color: var(--brand-blue);
    font-weight: 500;
    font-size: 25px;
    line-height: 1.45;
  }
  .contact-icon {
    width: 20px;
    height: 16px;
    flex: none;
  }
  .service-band {
    position: absolute;
    left: 0;
    bottom: 0;
    width: 100%;
    height: 58px;
    padding: 0 32px;
    background: var(--band-blue);
    display: flex;
    align-items: center;
    justify-content: center;
    color: var(--band-text);
    font-weight: 500;
    font-size: 16px;
    letter-spacing: 0.8px;
    text-transform: uppercase;
    white-space: pre;
  }
</style>
</head>
<body>
<main class="stage">
  <section class="business-card" aria-label="Business card">
    <div class="brand-lockup">
      <span class="brand-mark" aria-hidden="true"></span>
      <span class="brand-name">hallowell roof plumbing</span>
    </div>

    <div class="holder">
      <p class="holder-name">Owen Hallowell</p>
      <p class="holder-role">Owner</p>
    </div>

    <ul class="contact-list">
      <li class="contact-item">
        <svg class="contact-icon" viewBox="0 0 20 16" aria-label="Phone">
          <path d="M2 5 Q10 0 18 5 L16 7 L13 6 L13 4 Q10 3 7 4 L7 6 L4 7 Z" fill="var(--icon-grey)"/>
          <rect x="4" y="8" width="12" height="7" rx="1" fill="var(--icon-grey)"/>
        </svg>
        <span>0417 382 965</span>
      </li>
      <li class="contact-item">
        <svg class="contact-icon" viewBox="0 0 20 16" aria-label="Email">
          <rect x="1" y="2" width="18" height="12" fill="var(--icon-grey)"/>
          <path d="M1 2 L10 9 L19 2" fill="none" stroke="var(--card-black)" stroke-width="1.5"/>
        </svg>
        <span>owenhallowellroofing@maildrop-example.com</span>
      </li>
    </ul>

    <div class="service-band">Residential &amp; Commercial  -  Re-roof &amp; New Construction  -  Fully Insured</div>
  </section>
</main>
</body>
</html>
```